Reid Fallowmere - Senior Living Audio CDs - CD Design and Cover Design

I am an executive director in an assisted living facility. I have just started speaking, training, and coaching in the Senior Living Industry. I have 4 audio files that I want to put to a CD. The names of the CD's are:

1- Leadership - Creating A Culture of Excellence in Senior Living
2- The Purpose of Your Senior Living Business
3- A Leaders Vision - Your Attention Becomes Your Intention
4- Group Interviews -A Secret in Employee Retention

I think I can use the same CD cover for each CD. I just need the same design but 4 different ones with the names above. So everything will be the same but the name change. The inside cover will be I will consider other colors but it would be great if it would look good with the logo. I also need help with designing the CD face itself. I will be using a standard Jewel CD case. I need the front cover, the inside cover, and the back. The logo will be on all three.

On the front:

Part of me thinks it should be a clean simple design with my logo, my picture, and the title. But I am also curious about the picture of me with the elderly lady. - I need the 4 designs that are the same except the title.

On the Inside:

It can be the same design but the wording will be specific to that CD and the 4 insides will be:

All businesses rise and fall with leadership. This is especially true in the senior living industry. The life of that rise or fall is based on the culture the leader creates. Learn the 3 keys to what leaders know and do. Learn what the Importance Factor is and how you can put it to work to create and sustain a winning culture that will drive your business and occupancy above the rest.

What is the purpose of your senior living business? Your understanding to the answer of this question makes all the difference. After you have gained this understanding it takes the right beliefs and behavior of associates to fulfill this purpose. What's the purpose? How is it fulfilled?

They want a captain not a boss. As a leader in senior living you steer the ship. What you put your attention on becomes the intention of your community. Your ability to create a vision, help people embrace that vision, and learn how to stay focused when the storms of the industry come raging, is the key to your success. There is a pattern to achieving this success. Come learn this pattern and how to apply it in your life and your business. It can make all the difference.

A business can not be better than it's people. The right people are the key not just people. Learn where your focus should be to hire the right people. After you hire then find out what you can do to retain them and engage them. If you want happy residents you need happy associates.

On the back it will need to have:

1- My Logo
2- www.ReidFallowmere.example
3- Email: info@ReidFallowmere.example
4- You could put the picture of me and the elderly lady as a watermark on the back with the above info.

I have a short turn around time and need designs quickly. I also need help with designing the CD. My picture, the logo, and the Title.

```html
<!DOCTYPE html>
<html lang="en">
<head>
<meta charset="utf-8">
<title>Reid Fallowmere – Senior Living Audio Series Covers</title>
<link rel="stylesheet" href="https://fonts.googleapis.com/css2?family=Cinzel:wght@400;500&family=Arimo:wght@400&display=swap">
<style>
  :root {
    --page: #ffffff;
    --cover-light: #5c5c5c;
    --cover-dark: #1c1c1c;
    --accent-red: #c3241c;
    --type-light: #ffffff;
    --logo-card: #f4f2ee;
    --logo-ink: #2b2b2b;
    --logo-gold: #b8893a;
    --photo-top: #6b6460;
    --photo-mid: #2a2f3d;
    --photo-bottom: #15161c;
  }
  html, body {
    margin: 0;
    padding: 0;
    width: 900px;
    height: 1200px;
    overflow: hidden;
    background: var(--page);
  }
  .canvas {
    position: relative;
    width: 900px;
    height: 1200px;
  }
  .defs { position: absolute; width: 0; height: 0; }
  .cover {
    position: absolute;
    width: 422px;
    height: 422px;
    display: block;
  }
  .cover--vision { left: 22px; top: 28px; }
  .cover--interviews { left: 458px; top: 368px; }
  .cover--purpose { left: 24px; top: 727px; }

  .drop-letter {
    font-family: "Cinzel", "Trajan Pro", serif;
    font-weight: 400;
    font-size: 172px;
    fill: var(--accent-red);
  }
  .series-title {
    font-family: "Cinzel", "Trajan Pro", serif;
    font-weight: 400;
    font-size: 29px;
    fill: var(--type-light);
  }
  .tagline {
    font-family: "Arimo", Arial, sans-serif;
    font-size: 16px;
    fill: var(--type-light);
  }
  .rule { stroke: var(--accent-red); stroke-width: 1.6; }
  .logo-card { fill: var(--logo-card); }
  .logo-dot { fill: var(--logo-gold); }
  .logo-name {
    font-family: "Cinzel", serif;
    font-weight: 500;
    font-size: 7.5px;
    fill: var(--logo-ink);
  }
</style>
</head>
<body>
<main class="canvas">

  <svg class="defs" aria-hidden="true">
    <defs>
      <radialGradient id="backdrop" cx="55%" cy="40%" r="75%">
        <stop offset="0%" stop-color="var(--cover-light)"/>
        <stop offset="100%" stop-color="var(--cover-dark)"/>
      </radialGradient>
      <linearGradient id="portrait-tone" x1="0" y1="0" x2="0" y2="1">
        <stop offset="0%" stop-color="var(--photo-top)" stop-opacity="0.55"/>
        <stop offset="32%" stop-color="var(--photo-mid)" stop-opacity="0.9"/>
        <stop offset="100%" stop-color="var(--photo-bottom)"/>
      </linearGradient>
    </defs>
  </svg>

  <!-- Cover: A Leaders Vision -->
  <svg class="cover cover--vision" viewBox="0 0 422 422">
    <rect width="422" height="422" fill="url(#backdrop)"/>
    <rect x="148" y="30" width="262" height="392" rx="60" fill="url(#portrait-tone)"
          role="img" aria-label="Portrait of Reid Fallowmere in a dark suit and striped tie"/>
    <g class="logo">
      <rect class="logo-card" x="25" y="25" width="79" height="25"/>
      <circle class="logo-dot" cx="33" cy="37.5" r="4.5"/>
      <text class="logo-name" x="41" y="40" textLength="58" lengthAdjust="spacingAndGlyphs">Reid Fallowmere</text>
    </g>
    <line class="rule" x1="29" y1="307" x2="422" y2="307"/>
    <text class="drop-letter" x="27" y="309">A</text>
    <text class="series-title" x="90" y="296" textLength="206" lengthAdjust="spacingAndGlyphs">Leaders Vision</text>
    <text class="tagline" x="156" y="326">Your Attention</text>
    <text class="tagline" x="156" y="346">Becomes Your Intention</text>
  </svg>

  <!-- Cover: Group Interviews -->
  <svg class="cover cover--interviews" viewBox="0 0 422 422">
    <rect width="422" height="422" fill="url(#backdrop)"/>
    <rect x="140" y="28" width="272" height="394" rx="60" fill="url(#portrait-tone)"
          role="img" aria-label="Portrait of Reid Fallowmere in a dark suit and striped tie"/>
    <g class="logo">
      <rect class="logo-card" x="25" y="25" width="79" height="25"/>
      <circle class="logo-dot" cx="33" cy="37.5" r="4.5"/>
      <text class="logo-name" x="41" y="40" textLength="58" lengthAdjust="spacingAndGlyphs">Reid Fallowmere</text>
    </g>
    <line class="rule" x1="135" y1="287" x2="422" y2="287"/>
    <text class="series-title" x="28" y="279" textLength="76" lengthAdjust="spacingAndGlyphs">Group</text>
    <text class="drop-letter" x="106" y="306">I</text>
    <text class="series-title" x="139" y="279" textLength="114" lengthAdjust="spacingAndGlyphs">nterviews</text>
    <text class="tagline" x="149" y="323">A Secret in</text>
    <text class="tagline" x="149" y="343">Employee Retention</text>
  </svg>

  <!-- Cover: The Purpose of Your Senior Living Business -->
  <svg class="cover cover--purpose" viewBox="0 0 422 422">
    <rect width="422" height="422" fill="url(#backdrop)"/>
    <rect x="148" y="28" width="262" height="394" rx="60" fill="url(#portrait-tone)"
          role="img" aria-label="Portrait of Reid Fallowmere in a dark suit and striped tie"/>
    <g class="logo">
      <rect class="logo-card" x="25" y="25" width="79" height="25"/>
      <circle class="logo-dot" cx="33" cy="37.5" r="4.5"/>
      <text class="logo-name" x="41" y="40" textLength="58" lengthAdjust="spacingAndGlyphs">Reid Fallowmere</text>
    </g>
    <line class="rule" x1="0" y1="333" x2="286" y2="333"/>
    <text class="drop-letter" x="24" y="306">T</text>
    <text class="series-title" x="104" y="276" textLength="182" lengthAdjust="spacingAndGlyphs">he Purpose</text>
    <text class="tagline" x="286" y="296" text-anchor="end">of Your Senior</text>
    <text class="tagline" x="286" y="316" text-anchor="end">Living Business</text>
  </svg>

</main>
</body>
</html>
```